Corvane Flyer

Flyer needed for trade show. Main colors to use red, black, silver/grey. Logo attached. Please reference website for company details and any images that could be used. https://corvanesecuritywa.com/

Target Market(s)

Security

Industry/Entity Type

Security

Requirements
Must have
• Check website

```html
<!DOCTYPE html>
<html lang="en">
<head>
<meta charset="utf-8">
<title>Corvane Security Flyer</title>
<link rel="stylesheet" href="https://fonts.googleapis.com/css2?family=Bebas+Neue&family=Nunito+Sans:wght@400;600&display=swap">
<style>
:root{
  --navy:#111a26;
  --orange:#ee4b22;
  --ice:#eaf3fa;
  --white:#ffffff;
  --stage:#e1e1e1;
  --photo-light:#c9ccd0;
  --photo-dark:#3a3f47;
}
*{margin:0;padding:0;box-sizing:border-box}
html,body{width:681px;height:1200px;overflow:hidden;background:var(--stage)}
.canvas{position:relative;width:681px;height:1200px}
.flyer{position:absolute;left:0;top:159px;width:824px;height:1067px;transform:scale(0.8265);transform-origin:0 0;background:var(--navy);overflow:hidden;font-family:"Nunito Sans",Arial,sans-serif}
.shapes{position:absolute;inset:0}
.display{position:absolute;font-family:"Bebas Neue",Impact,sans-serif;line-height:1;white-space:nowrap}
.brand{left:0;top:62px;width:200px;text-align:center;font-size:40px;color:var(--orange);letter-spacing:3px}
.headline{left:18px;top:380px;font-size:104px;color:var(--white)}
.subhead{left:20px;top:470px;font-size:50px;color:var(--navy)}
.about-title{right:30px;text-align:right;font-size:30px;color:var(--white)}
.about-title.first{top:354px}
.about-title.second{top:383px;border-bottom:2px solid var(--orange)}
.about-text{position:absolute;right:26px;top:424px;width:310px;text-align:right;font-size:13px;line-height:19px;color:var(--white)}
.industries{left:20px;top:542px;font-size:82px;color:var(--navy)}
.we-serve{left:20px;top:602px;font-size:124px;color:var(--navy)}
.standing{right:24px;top:538px;font-size:116px;color:var(--navy);transform:scaleX(0.93);transform-origin:right top}
.guard-service{right:18px;top:641px;font-size:78px;color:var(--navy);transform:scaleX(0.88);transform-origin:right top}
.services-tag{left:27px;top:717px;height:43px;padding:8px 6px 0;background:var(--orange);font-size:30px;color:var(--navy)}
.service{position:absolute;left:28px;width:300px}
.service h3{font-family:"Bebas Neue",Impact,sans-serif;font-weight:400;font-size:21px;line-height:1;color:var(--navy);display:inline-block;border-bottom:1px solid var(--orange);padding-bottom:3px;width:152px}
.service p{font-size:12.5px;line-height:20px;color:var(--navy);margin-top:3px}
.benefits{position:absolute;right:28px;top:739px;list-style:none;text-align:right}
.benefits li{font-size:17px;font-weight:600;line-height:29px;color:var(--navy)}
.benefits li::after{content:"";display:inline-block;width:10px;height:10px;border-radius:50%;background:var(--orange);margin-left:14px;vertical-align:1px}
.phone{right:32px;top:935px;font-size:50px;color:var(--white)}
.contact-line{right:32px;font-size:23px;color:var(--white)}
.contact-line.email{top:990px}
.contact-line.address{top:1022px}
.icon{position:absolute}
.social{position:absolute;top:1016px;width:26px;height:26px;background:var(--white);border-radius:3px}
.footer-name{left:173px;top:1017px;font-size:25px;color:var(--white)}
</style>
</head>
<body>
<div class="canvas">
  <div class="flyer">
    <svg class="shapes" width="824" height="1067" viewBox="0 0 824 1067">
      <rect x="0" y="0" width="824" height="1067" fill="var(--ice)"/>
      <polygon points="0,0 824,0 824,533 441,533 489,380 0,380" fill="var(--navy)"/>
      <polygon role="img" aria-label="Photo of a security guard in a cap and earpiece looking out a window" points="170,118 218,0 570,0 630,130 505,380 0,380 0,118" fill="var(--photo-light)"/>
      <polygon points="570,0 625,0 690,130 560,380 505,380 630,130" fill="var(--orange)"/>
      <polygon points="0,380 489,380 441,533 0,533" fill="var(--orange)"/>
      <polygon role="img" aria-label="Photo of a uniformed security officer wearing sunglasses" points="502,246 544,132 702,132 764,246 702,360 544,360" fill="var(--photo-dark)" stroke="var(--orange)" stroke-width="4"/>
      <polygon points="394,533 824,533 824,725 456,725" fill="var(--orange)"/>
      <polygon points="484,918 824,918 824,1067 324,1067" fill="var(--orange)"/>
      <polygon points="0,996 370,996 324,1067 0,1067" fill="var(--navy)"/>
      <polygon role="img" aria-label="Security guard icon" points="334,878 379,800 469,800 514,878 469,956 379,956" fill="var(--navy)" stroke="var(--orange)" stroke-width="3"/>
    </svg>

    <div class="display brand">Corvane</div>

    <div class="display headline">Exceptional</div>
    <div class="display subhead">Security Guard Solutions</div>

    <div class="display about-title first">About</div>
    <div class="display about-title second">Corvane Security</div>
    <p class="about-text">Corvane Security Services provides top-tier security with 24/7 monitoring, patrols, access control, and firewatch. As the #1 patrol service, we ensure swift response and round-the-clock protection.</p>

    <div class="display industries">Industries</div>
    <div class="display we-serve">We Serve</div>
    <div class="display standing">Standing</div>
    <div class="display guard-service">Guard Service</div>

    <div class="display services-tag">Our Services</div>
    <div class="service" style="top:773px"><h3>Firewatch Services</h3><p>Corvane Security Solutions, we understand the critical</p></div>
    <div class="service" style="top:846px;width:320px"><h3>Mobile Patrol</h3><p>Stay secure with our dynamic and adaptable Mobile Patrol Services–flexible protection for your property!</p></div>
    <div class="service" style="top:919px;width:320px"><h3>24/7 Dispatcht</h3><p>Corvane Security Solutions provides 24/7 Dispatch Services for instant response to any security emergen-</p></div>

    <ul class="benefits">
      <li>Expertise &amp; Experience</li>
      <li>Rapid Response Times</li>
      <li>Proven Track Record</li>
      <li>Security Solutions</li>
      <li>Highly Trained</li>
      <li>24/7 Availability</li>
    </ul>

    <svg class="icon" style="left:500px;top:938px" width="40" height="40" viewBox="0 0 24 24">
      <path d="M6.6 10.8a15.1 15.1 0 0 0 6.6 6.6l2.2-2.2a1 1 0 0 1 1-.25 11.4 11.4 0 0 0 3.6.57 1 1 0 0 1 1 1V20a1 1 0 0 1-1 1A17 17 0 0 1 3 4a1 1 0 0 1 1-1h3.5a1 1 0 0 1 1 1c0 1.25.2 2.45.57 3.57a1 1 0 0 1-.25 1z" fill="var(--navy)"/>
    </svg>
    <div class="display phone">(206) 555-0148</div>
    <svg class="icon" style="left:497px;top:990px" width="28" height="20" viewBox="0 0 28 20">
      <rect x="1" y="1" width="26" height="18" fill="none" stroke="var(--white)" stroke-width="2"/>
      <polyline points="1,1 14,11 27,1" fill="none" stroke="var(--white)" stroke-width="2"/>
    </svg>
    <div class="display contact-line email">Office@corvanesecuritywa.com</div>
    <div class="display contact-line address">1420 Harbor Lane, Kent, WA 98032, USA</div>

    <div class="social" style="left:30px"></div>
    <div class="social" style="left:80px"></div>
    <div class="social" style="left:130px"></div>
    <div class="display footer-name">Corvane Security</div>
  </div>
</div>
</body>
</html>
```